Business Card Design for Mabel's Pantry

We make food for dogs.
Business Card Design (using the logo designed by you). Our Brand color is a bright canary yellow. For example our signage is predominantly yellow, with the logo in black. I'd like the card also to use that imagery.
Feel free to use the two sides creatively.
Vertical Design is also great.

Industry/Entity Type

Pet food

Contact Information for Business Card

Name, email, website, phone no

Font styles to use
Sans Serif

Colors
59FF00
82FF00
B8FF75
E3FFCB
F4FFEA
FFF300
FFF600
FEFA6F
FFFEC7
FFFEE8

Requirements
Nice to have
• A graphic in the same brush stroke style of the logo shoeing a doggy bowl of food

```html
<!DOCTYPE html>
<html lang="en">
<head>
<meta charset="utf-8">
<title>Mabel's Pantry — Business Card</title>
<link rel="stylesheet" href="https://fonts.googleapis.com/css2?family=Bebas+Neue&family=Roboto:wght@400&display=swap">
<style>
  :root {
    --canary: #FFE14D;
    --ink: #000000;
    --paper-top: #f6f1f1;
    --paper-bottom: #efe6e6;
    --stage: #e9e9eb;
    --white: #ffffff;
  }
  * { margin: 0; padding: 0; box-sizing: border-box; }
  html, body {
    width: 1200px;
    height: 900px;
    overflow: hidden;
    background: var(--stage);
  }
  .business-card {
    position: absolute;
    left: 100px;
    top: 140px;
    width: 1000px;
    height: 620px;
    box-shadow: 0 10px 30px rgba(0,0,0,0.18);
  }
  .business-card svg { display: block; width: 100%; height: 100%; }
  .card-paper-stop-top { stop-color: var(--paper-top); }
  .card-paper-stop-bottom { stop-color: var(--paper-bottom); }
  .ink-band { fill: var(--ink); }
  .band-edge { fill: none; stroke: var(--canary); stroke-width: 6; stroke-linecap: round; }
  .brand-name {
    font-family: "Bebas Neue", sans-serif;
    font-size: 112px;
    fill: var(--canary);
  }
  .person-name {
    font-family: "Bebas Neue", sans-serif;
    font-size: 58px;
    fill: var(--canary);
  }
  .person-role, .contact-line, .address-line {
    font-family: "Roboto", sans-serif;
    font-size: 30px;
    fill: var(--white);
  }
  .address-line { text-anchor: end; }
  .highlight { fill: var(--canary); }
  .contact-icon { fill: var(--canary); }
  .contact-icon-line { fill: none; stroke: var(--canary); stroke-width: 2; }
</style>
</head>
<body>
<div class="business-card">
  <svg viewBox="0 0 1086 673" xmlns="http://www.w3.org/2000/svg">
    <defs>
      <linearGradient id="card-paper" x1="0" y1="0" x2="0" y2="1">
        <stop offset="0" class="card-paper-stop-top"/>
        <stop offset="1" class="card-paper-stop-bottom"/>
      </linearGradient>
    </defs>

    <rect class="card-paper" width="1086" height="673" fill="url(#card-paper)"/>

    <path class="ink-band" d="M0,330 C320,300 620,520 1086,440 L1086,673 L0,673 Z"/>
    <path class="band-edge" d="M0,330 C320,300 620,520 1086,440"/>

    <text class="brand-name" x="510" y="296" textLength="530" lengthAdjust="spacingAndGlyphs">MABEL'S PANTRY</text>

    <text class="person-name" x="60" y="432">DANIEL HART</text>
    <text class="person-role" x="60" y="466">Managing Director</text>

    <g class="contact-phone">
      <path class="contact-icon" d="M64,506 c3,-2 6,-2 8,1 l4,6 c1,2 0,4 -2,5 l-3,2 c2,5 6,9 11,11 l2,-3 c1,-2 3,-3 5,-2 l6,4 c3,2 3,5 1,8 l-3,3 c-14,1 -33,-18 -32,-32 z"/>
      <text class="contact-line" x="98" y="530">044-555 010 234</text>
    </g>
    <g class="contact-email">
      <rect class="contact-icon" x="60" y="551" width="30" height="20"/>
      <path d="M60,551 L75,563 L90,551" fill="none" stroke="#000" stroke-width="2"/>
      <text class="contact-line" x="98" y="570">hello@mabelspantry.com</text>
    </g>
    <g class="contact-web">
      <circle class="contact-icon-line" cx="75" cy="600" r="13"/>
      <ellipse class="contact-icon-line" cx="75" cy="600" rx="6" ry="13"/>
      <line class="contact-icon-line" x1="62" y1="600" x2="88" y2="600"/>
      <line class="contact-icon-line" x1="64" y1="593" x2="86" y2="593"/>
      <line class="contact-icon-line" x1="64" y1="607" x2="86" y2="607"/>
      <text class="contact-line" x="98" y="610">www.<tspan class="highlight">mabelspantry</tspan>.com</text>
    </g>

    <text class="address-line" x="990" y="570">421, Address</text>
    <text class="address-line" x="990" y="610">line here ,Country Name</text>
  </svg>
</div>
</body>
</html>
```